RT Pemberly Electric Yard Sign

Looking to have a yard sign designed that we can place at projects we are working on. Most likely will be 18" H x 24" W but flexible that we can increase the size if necessary. It should include our logo, our phone # 609-555-0147, website rtpemberlyelectric-example.com and slogan, built on integrity, driven by excellence. Colors should match our brand.

```html
<!DOCTYPE html>
<html lang="en">
<head>
<meta charset="utf-8">
<title>RT Pemberly Electric Yard Sign</title>
<link href="https://fonts.googleapis.com/css2?family=Montserrat:wght@800&family=Poppins:ital,wght@0,500;1,500&family=Roboto:wght@900&display=swap" rel="stylesheet">
<style>
  :root {
    --red: #d6201f;
    --red-dark: #b81a1a;
    --navy: #1b3466;
    --navy-deep: #142a55;
    --paper: #f5f5f5;
    --edge: #c9ccd2;
    --backdrop: #e7e9ec;
    --white: #ffffff;
  }
  html, body {
    margin: 0;
    width: 1200px;
    height: 1200px;
    overflow: hidden;
    background: var(--backdrop);
  }
  .yard-sign {
    position: absolute;
    left: 100px;
    top: 187px;
    width: 1000px;
    height: 825px;
    box-shadow: 0 18px 40px rgba(0,0,0,0.18);
  }
  .sign-shapes {
    position: absolute;
    inset: 0;
  }
  .sign-text {
    position: absolute;
    left: 0;
    width: 100%;
    text-align: center;
    margin: 0;
  }
  .company-name {
    top: 200px;
    font-family: "Montserrat", sans-serif;
    font-weight: 800;
    font-size: 76px;
    letter-spacing: 4px;
    color: var(--red);
  }
  .trade-line {
    top: 303px;
    font-family: "Montserrat", sans-serif;
    font-weight: 800;
    font-size: 42px;
    letter-spacing: 9px;
    color: var(--navy);
  }
  .phone {
    top: 496px;
    font-family: "Roboto", sans-serif;
    font-weight: 900;
    font-size: 108px;
    line-height: 1;
    color: var(--white);
  }
  .website {
    top: 624px;
    font-family: "Poppins", sans-serif;
    font-weight: 500;
    font-size: 40px;
    line-height: 1;
    color: var(--white);
  }
  .slogan {
    top: 716px;
    font-family: "Poppins", sans-serif;
    font-style: italic;
    font-weight: 500;
    font-size: 35px;
    line-height: 1;
    color: var(--white);
    display: flex;
    justify-content: center;
    align-items: center;
    gap: 26px;
  }
  .slogan-divider {
    width: 3px;
    height: 40px;
    background: var(--navy);
  }
</style>
</head>
<body>
  <div class="yard-sign">
    <svg class="sign-shapes" viewBox="0 0 1000 825" width="1000" height="825">
      <rect class="navy-field" width="1000" height="825" fill="var(--navy)"/>
      <polygon class="upper-red-rule" points="0,392 50,458 950,458 1000,392 1000,430 955,475 45,475 0,430" fill="var(--red)"/>
      <polygon class="white-panel-edge" points="0,0 1000,0 1000,392 950,446 50,446 0,392" fill="var(--edge)"/>
      <polygon class="white-panel" points="0,0 1000,0 1000,385 955,438 45,438 0,385" fill="var(--paper)"/>
      <polygon class="corner-left" points="0,0 110,0 0,110" fill="var(--red)"/>
      <polygon class="corner-right" points="1000,0 890,0 1000,110" fill="var(--red)"/>
      <line class="underline-red" x1="108" y1="362" x2="905" y2="362" stroke="var(--red)" stroke-width="4"/>
      <line class="underline-navy" x1="120" y1="369" x2="895" y2="369" stroke="var(--navy)" stroke-width="4"/>
      <polygon class="slogan-band-edge" points="0,688 1000,684 1000,744 958,790 42,790 0,744" fill="var(--edge)"/>
      <polygon class="slogan-band" points="0,690 1000,686 1000,738 962,780 38,780 0,738" fill="var(--red-dark)"/>
      <rect class="bottom-strip" y="790" width="1000" height="35" fill="var(--navy-deep)"/>
    </svg>

    <p class="sign-text company-name">RT PEMBERLY</p>
    <p class="sign-text trade-line">Electrical Contractor</p>
    <p class="sign-text phone">609-555-0147</p>
    <p class="sign-text website">rtpemberlyelectric-example.com</p>
    <p class="sign-text slogan"><span>Built on Integrity</span><span class="slogan-divider"></span><span>Driven by Excellence</span></p>
  </div>
</body>
</html>
```